Business cards for a high-end menswear store

I would like to come up with a design for our business cards.
Two different ones: one for general sales and one for the owner. It is a high-end menswear store.

Our address is: 4817 Valmonde Boulevard, Montreal, QC, H2R4K7
phone number: 514-582-3960
insta: MAISONVERLAINT
Website: www.maisonverlaint.com
email (general card): info@maisonverlaint.com
email (owner): morvin@maisonverlaint.com

I have attached our logo in an ai and eps file format. You can see our old cards as well. I am looking for a modern and clean look.

Target Market(s)

High-End Clothing Market

Industry/Entity Type

Retail, Clothing, Luxury Clothing

Contact Information for Business Card

Address, Name, Email, Website, Social Info,

Font styles to use
Serif

Colors

Designer to choose colors to be used in the design.

Requirements
Must have
• Address, Name, Email, Website, Social Info,
Nice to have
• QR Code that brings you to the website

```html
<!DOCTYPE html>
<html lang="en">
<head>
<meta charset="utf-8">
<title>Maison Verlaint — Owner Business Card</title>
<link rel="stylesheet" href="https://fonts.googleapis.com/css2?family=Jost:wght@300;400&family=Playfair+Display:wght@500&display=swap">
<style>
  :root {
    --backdrop: #c8c8c6;
    --card: #f7f7f5;
    --ink: #1b1b1b;
    --ink-soft: #3a3a3a;
  }
  * { margin: 0; padding: 0; box-sizing: border-box; }
  html, body {
    width: 1200px;
    height: 900px;
    overflow: hidden;
    background: var(--backdrop);
  }
  .stage {
    width: 1200px;
    height: 900px;
    display: flex;
    align-items: center;
    justify-content: center;
  }
  .business-card {
    position: relative;
    width: 640px;
    height: 640px;
    background: var(--card);
    box-shadow: 0 18px 40px rgba(0, 0, 0, 0.12);
    color: var(--ink);
    font-family: "Jost", sans-serif;
  }
  .brand-mark {
    position: absolute;
    top: 112px;
    right: 70px;
    display: flex;
    flex-direction: column;
    align-items: flex-end;
    gap: 8px;
  }
  .brand-name {
    font-family: "Jost", sans-serif;
    font-weight: 400;
    font-size: 11px;
    letter-spacing: 0.32em;
    text-transform: uppercase;
    color: var(--ink);
  }
  .brand-square {
    width: 112px;
    height: 112px;
    background: var(--ink);
  }
  .holder {
    position: absolute;
    top: 196px;
    left: 72px;
  }
  .holder-name {
    font-family: "Playfair Display", serif;
    font-weight: 500;
    font-size: 40px;
    letter-spacing: 0.03em;
    line-height: 1;
  }
  .holder-role {
    margin-top: 12px;
    font-weight: 300;
    font-size: 19px;
    letter-spacing: 0.34em;
    color: var(--ink-soft);
  }
  .contact-list {
    position: absolute;
    top: 312px;
    left: 72px;
    list-style: none;
    font-weight: 400;
    font-size: 20px;
    letter-spacing: 0.06em;
    line-height: 1.35;
  }
  .contact-item {
    display: flex;
    align-items: flex-start;
    gap: 14px;
    margin-bottom: 10px;
  }
  .contact-icon {
    flex: 0 0 20px;
    width: 20px;
    height: 20px;
    margin-top: 3px;
    fill: none;
    stroke: var(--ink);
    stroke-width: 1.4;
    stroke-linecap: round;
    stroke-linejoin: round;
  }
</style>
</head>
<body>
<main class="stage">
  <article class="business-card">
    <div class="brand-mark">
      <span class="brand-name">Maison Verlaint</span>
      <div class="brand-square"></div>
    </div>

    <header class="holder">
      <h1 class="holder-name">Morvin Verlaint</h1>
      <p class="holder-role">owner</p>
    </header>

    <ul class="contact-list">
      <li class="contact-item">
        <svg class="contact-icon" viewBox="0 0 20 20" aria-hidden="true">
          <path d="M10 18s6-6 6-10.5a6 6 0 0 0-12 0C4 12 10 18 10 18z"/>
          <circle cx="10" cy="7.5" r="2.2"/>
        </svg>
        <span>4817 Valmonde Boulevard,<br>Montreal, QC, H2R4K7</span>
      </li>
      <li class="contact-item">
        <svg class="contact-icon" viewBox="0 0 20 20" aria-hidden="true">
          <rect x="5" y="2" width="10" height="16" rx="1.6"/>
          <line x1="5" y1="14.5" x2="15" y2="14.5"/>
        </svg>
        <span>514-582-3960</span>
      </li>
      <li class="contact-item">
        <svg class="contact-icon" viewBox="0 0 20 20" aria-hidden="true">
          <circle cx="10" cy="10" r="7"/>
        </svg>
        <span>MAISONVERLAINT</span>
      </li>
      <li class="contact-item">
        <svg class="contact-icon" viewBox="0 0 20 20" aria-hidden="true">
          <circle cx="10" cy="10" r="8"/>
          <ellipse cx="10" cy="10" rx="3.5" ry="8"/>
          <line x1="2" y1="10" x2="18" y2="10"/>
        </svg>
        <span>www.maisonverlaint.com</span>
      </li>
      <li class="contact-item">
        <svg class="contact-icon" viewBox="0 0 20 20" aria-hidden="true">
          <rect x="2" y="4.5" width="16" height="11" rx="1"/>
          <polyline points="2.5,5 10,11 17.5,5"/>
        </svg>
        <span>morvin@maisonverlaint.com</span>
      </li>
    </ul>
  </article>
</main>
</body>
</html>
```